Business Card/ Car Magnet/ Polo Shirt/ Envelope/ Letterhead Design Project
Birchmont Property Valuations, LLC.
Business Card/ Car Magnet/ Polo Shirt/ Envelope/ Letterhead Design Project - Real Estate
Creative Brief
Professional
Gus Talbottine
State Certified Residential Real Estate Appraiser
14 Coldmeadow Ln Sewell, NJ 08080
gtalbottine@birchmontvaluations.example
valuemarkhq.example
NJ- 57RC00913400 PA- RL284615 DE- X2-0000317
Please be creative...
gust1983 gust1983
Hello, Just wanted to clarify some of the common questions asked so far. The colors to incorporate would be blue, green and white (unless of course you would like to incorporate other colors for creativity) . please feel free to incorporate them any way you see fit. The polo shirts will be done on white, black and royal blue shirts. Please be as creative as you like. Thanks you for your efforts and for participating! Please reply back with any further questions. Thanks! BPV

```html
<!DOCTYPE html>
<html lang="en">
<head>
<meta charset="utf-8">
<title>Birchmont Property Valuations – Business Card</title>
<link href="https://fonts.googleapis.com/css2?family=Open+Sans:wght@400;600;700&display=swap" rel="stylesheet">
<style>
  :root{
    --backdrop:#2a2a2c;
    --card:#ffffff;
    --brand-blue:#1f5fa8;
    --band-blue:#2f86d6;
    --band-deep:#1d62b5;
    --accent-green:#5aa832;
    --ink:#3a3a3a;
    --muted:#777b80;
  }
  *{margin:0;padding:0;box-sizing:border-box}
  html,body{width:1200px;height:698px;overflow:hidden;background:var(--backdrop)}
  body{font-family:"Open Sans",Arial,sans-serif;position:relative}
  .card{position:absolute;top:194px;width:540px;height:310px;border-radius:18px;background:var(--card);overflow:hidden;box-shadow:0 6px 18px rgba(0,0,0,.35)}
  .card--back{left:40px}
  .card--front{left:620px}
  .brand{display:flex;flex-direction:column;align-items:center;color:var(--brand-blue);font-weight:700}
  .brand__row{display:flex;align-items:center;gap:10px}
  .brand__dot{width:18px;height:18px;border-radius:50%;background:var(--accent-green)}
  .brand__initials{font-size:46px;letter-spacing:3px;line-height:1}
  .brand__name{font-size:9px;letter-spacing:1.2px;margin-top:6px;border-top:1.5px solid var(--brand-blue);padding-top:4px;text-transform:uppercase}
  .card--back .brand{position:absolute;top:62px;left:0;right:0}
  .website{position:absolute;top:205px;left:0;right:0;text-align:center;font-size:13px;letter-spacing:5px;color:var(--ink)}
  .card--front .brand{position:absolute;top:36px;left:30px}
  .card--front .brand__initials{font-size:36px}
  .card--front .brand__name{font-size:7px}
  .front-art{position:absolute;inset:0}
  .person{position:absolute;left:34px;top:188px;color:var(--brand-blue)}
  .person__name{font-size:12px;font-weight:700;letter-spacing:1px}
  .person__title{font-size:9px;color:var(--muted);letter-spacing:1px;margin-top:1px}
  .address{position:absolute;left:34px;top:262px;color:#fff;font-size:9px;line-height:1.5}
  .contacts{position:absolute;right:22px;top:132px;list-style:none;color:#fff;font-size:8.5px}
  .contacts li{display:flex;align-items:center;justify-content:flex-end;gap:7px;height:19px;white-space:nowrap}
  .contacts svg{width:11px;height:11px;flex:none;fill:none;stroke:#fff;stroke-width:1.6}
</style>
</head>
<body>
  <section class="card card--back">
    <div class="brand">
      <div class="brand__row"><span class="brand__dot"></span><span class="brand__initials">BPV</span></div>
      <div class="brand__name">Birchmont Property Valuations, LLC.</div>
    </div>
    <p class="website">www.valuemarkhq.example</p>
  </section>

  <section class="card card--front">
    <svg class="front-art" viewBox="0 0 540 310" preserveAspectRatio="none">
      <defs>
        <linearGradient id="band" x1="0" y1="0" x2="1" y2="1">
          <stop offset="0" stop-color="var(--band-blue)"/>
          <stop offset="1" stop-color="var(--band-deep)"/>
        </linearGradient>
      </defs>
      <path d="M400 0 L540 0 L540 310 L0 310 L0 250 C200 245 380 190 400 0 Z" fill="url(#band)"/>
      <path d="M388 0 C362 183 190 238 0 242" fill="none" stroke="var(--accent-green)" stroke-width="4"/>
    </svg>
    <div class="brand">
      <div class="brand__row"><span class="brand__dot"></span><span class="brand__initials">BPV</span></div>
      <div class="brand__name">Birchmont Property Valuations, LLC.</div>
    </div>
    <div class="person">
      <p class="person__name">GUS TALBOTTINE</p>
      <p class="person__title">PRESIDENT</p>
    </div>
    <p class="address">14 Coldmeadow Ln<br>Sewell, NJ 08080</p>
    <ul class="contacts">
      <li>+1 856 555 0142<svg viewBox="0 0 12 12"><path d="M3 1l2 2-1 2 3 3 2-1 2 2-2 2C5 10 2 7 1 3z"/></svg></li>
      <li>+1 856 555 0178<svg viewBox="0 0 12 12"><rect x="3" y="1" width="6" height="10" rx="1"/></svg></li>
      <li>gtalbottine@birchmontvaluations.example<svg viewBox="0 0 12 12"><rect x="1" y="3" width="10" height="7"/><path d="M1 3l5 4 5-4"/></svg></li>
      <li>www.valuemarkhq.example<svg viewBox="0 0 12 12"><circle cx="6" cy="6" r="5"/><path d="M1 6h10M6 1c3 3 3 7 0 10M6 1c-3 3-3 7 0 10"/></svg></li>
    </ul>
  </section>
</body>
</html>
```